IT Company based on Biology Business Needs a Professional Web Design

We need a professional business website design for a new company called 'Vast KELP'. We develop the machine learning solutions especially focused on deep learning algorithms for biology industry. Our initial product is a vision detection on biological images to help doctors diagnose the symptoms. We would like to see designs that use the color green.

Industry/Entity Type

Business

Number of Pages Required

5+ page

```html
<!DOCTYPE html>
<html lang="en">
<head>
<meta charset="utf-8">
<title>Vast KELP – Biological Services</title>
<link rel="stylesheet" href="https://fonts.googleapis.com/css2?family=Montserrat:wght@400;600;700&family=Open+Sans:wght@400;600;700&display=swap">
<style>
:root{
  --green:#70b02a;
  --green-dark:#5d9820;
  --ink:#2b2b2b;
  --text:#666;
  --muted:#999;
  --band:#f7f7f7;
  --grey:#efefef;
  --line:#dcdcdc;
  --footer:#25262b;
  --footer-card:#2e2f35;
  --footer-bottom:#1b1c20;
  --white:#fff;
}
*{box-sizing:border-box;margin:0;padding:0}
html,body{width:1200px;height:2278px;overflow:hidden}
body{position:relative;background:var(--white);font-family:"Open Sans",Arial,sans-serif;color:var(--text)}
.abs{position:absolute}
h1,h2,h3,h4{font-family:"Montserrat",Arial,sans-serif;font-weight:600;color:var(--ink)}

/* header */
.site-header{position:absolute;left:0;top:0;width:1200px;height:79px;background:var(--white)}
.brand{position:absolute;left:150px;top:24px;display:flex;align-items:center;gap:8px;font-family:"Open Sans",Arial,sans-serif;font-weight:700;font-size:20px;color:var(--green);letter-spacing:.5px}
.brand-dot{width:14px;height:14px;border-radius:50%;background:var(--green)}
.nav a{position:absolute;top:26px;font-size:10.5px;color:var(--ink);text-decoration:none;text-transform:uppercase;padding:4px 10px;line-height:16px;white-space:nowrap}
.nav a.active{background:#2b2b2b;color:var(--white)}
.btn-contact{position:absolute;left:960px;top:21px;width:90px;height:34px;background:var(--green);color:var(--white);font-size:11px;font-weight:600;text-align:center;line-height:34px;border-bottom:3px solid var(--green-dark)}

/* hero */
.hero{position:absolute;left:0;top:79px;width:1200px;height:476px;overflow:hidden}
.hero-media{position:absolute;inset:0;background:linear-gradient(100deg,#e9f1f7 0%,#cfe0ec 35%,#7ea9cc 65%,#2f6fa6 100%)}
.hero-welcome{position:absolute;left:151px;top:156px;font-family:"Montserrat",sans-serif;font-size:21px;color:var(--green);text-transform:uppercase;letter-spacing:.3px;line-height:26px}
.hero-welcome span{color:#3a3a3a}
.hero-title{position:absolute;left:151px;top:180px;font-size:32px;line-height:40px;color:#3a3a3a;font-weight:600}
.hero-title span{color:var(--green)}
.hero-text{position:absolute;left:152px;top:226px;width:400px;font-size:10px;line-height:18px;color:#222;font-weight:600}
.btn-dark{position:absolute;left:152px;top:279px;width:88px;height:28px;background:#333;color:var(--white);font-size:12px;font-weight:600;line-height:28px;text-align:center;border-radius:2px}

/* features */
.features{position:absolute;left:0;top:555px;width:1200px;height:186px;background:var(--band)}
.feature{position:absolute;top:58px;width:280px}
.feature svg{position:absolute;left:0;top:0}
.feature h3{position:absolute;left:55px;top:0;font-size:14px;font-family:"Open Sans",sans-serif;font-weight:600;white-space:nowrap}
.feature p{position:absolute;left:55px;top:30px;width:225px;font-size:10.5px;line-height:23px;color:var(--muted)}

/* who we are */
.about-media{position:absolute;left:577px;top:741px;width:623px;height:371px;background:linear-gradient(90deg,#ffffff 0%,#eaf1f6 25%,#cfdde8 60%,#a9c4d8 100%)}
.about h2{position:absolute;left:151px;top:796px;font-size:22px}
.about p{position:absolute;left:151px;width:440px;font-size:10px;line-height:22.5px;color:var(--text)}
.btn-green{position:absolute;left:150px;top:1004px;width:91px;height:33px;background:var(--green);color:var(--white);font-size:12px;line-height:33px;text-align:center}

/* news & testimonials */
.grey-band{position:absolute;left:0;top:1112px;width:1200px;height:377px;background:var(--grey)}
.section-title{position:absolute;font-size:21px;text-transform:uppercase}
.pager{position:absolute;display:flex;gap:2px}
.pager span{width:12px;height:12px;background:#888;border-radius:2px;display:block;position:relative}
.pager span svg{position:absolute;left:3px;top:3px}
.news-card{position:absolute;left:150px;top:1198px;width:544px;height:245px;background:var(--white);border:1px solid var(--line)}
.news-head{position:absolute;left:66px;top:22px;width:270px;font-size:13px;line-height:19px;color:#777}
.news-head em{font-style:normal;color:var(--green)}
.news-photo{position:absolute;left:55px;top:88px;width:130px;height:77px;background:linear-gradient(135deg,#c98a6a,#8a5a48 50%,#3f4a6a)}
.news-body{position:absolute;left:200px;top:86px;width:312px;height:85px;overflow:hidden;font-size:10.5px;line-height:17px;color:#333}
.news-more{position:absolute;left:53px;top:181px;width:460px;font-size:10.5px;line-height:17px;color:#333}
.scroll-track{position:absolute;left:524px;top:22px;width:3px;height:200px;background:#e4e4e4;border-radius:2px}
.scroll-thumb{position:absolute;left:524px;top:52px;width:3px;height:60px;background:#888;border-radius:2px}
.quote-card{position:absolute;left:720px;top:1198px;width:328px;height:159px;background:var(--white);border:1px solid var(--line)}
.quote-card p{position:absolute;left:17px;top:16px;width:300px;font-size:12px;line-height:19.5px;color:#444}
.quote-tail{position:absolute;left:745px;top:1356px}
.avatar{position:absolute;left:722px;top:1389px;width:54px;height:54px;border-radius:50%;background:linear-gradient(180deg,#5b4a42,#d9c2b2)}
.person-name{position:absolute;left:785px;top:1405px;font-size:13px;color:var(--green);text-transform:uppercase;font-family:"Montserrat",sans-serif}
.person-place{position:absolute;left:785px;top:1422px;font-size:14px;color:#777}

/* services */
.services h2{position:absolute;left:0;width:1200px;top:1547px;text-align:center;font-size:21px}
.services .lead{position:absolute;left:0;width:1200px;top:1577px;text-align:center;font-size:11px;color:var(--text)}
.service{position:absolute;top:1640px;width:280px;text-align:center}
.service-art{margin:0 auto;width:140px;height:125px;border-radius:70px 70px 6px 6px}
.service h3{margin-top:28px;font-size:17px;font-family:"Open Sans",sans-serif;font-weight:600;letter-spacing:.5px}
.service p{margin-top:18px;font-size:10.5px;line-height:17.5px;color:var(--text)}
.service a{display:block;margin-top:16px;font-size:11.5px;font-weight:600;color:var(--green);text-decoration:none}

/* footer */
.site-footer{position:absolute;left:0;top:1970px;width:1200px;height:257px;background:var(--footer)}
.footer-col h4{position:absolute;top:2016px;font-size:17px;color:var(--white);font-weight:400}
.footer-col p,.footer-col li{font-size:10px;line-height:23px;color:#9a9ba0}
.footer-about{position:absolute;left:153px;top:2044px;width:250px}
.footer-news{position:absolute;left:451px;width:270px;height:62px;background:var(--footer-card)}
.footer-news .thumb{position:absolute;left:6px;top:6px;width:55px;height:50px;background:linear-gradient(135deg,#7fb0d6,#2f5f86)}
.footer-news .t{position:absolute;left:68px;top:4px;font-size:12px;color:var(--green)}
.footer-news .s{position:absolute;left:68px;top:20px;font-size:10px;color:#bbb;white-space:nowrap}
.footer-news .m{position:absolute;left:68px;top:35px;font-size:10.5px;color:var(--white);font-weight:600}
.footer-contact{position:absolute;left:769px;top:2044px;width:180px}
.footer-links{position:absolute;left:961px;top:2044px;list-style:none}
.footer-bottom{position:absolute;left:0;top:2227px;width:1200px;height:51px;background:var(--footer-bottom);font-size:10.5px;color:var(--white)}
.footer-bottom .copy{position:absolute;left:153px;top:18px}
.footer-bottom .legal{position:absolute;right:149px;top:18px}
</style>
</head>
<body>

<header class="site-header">
  <div class="brand"><span class="brand-dot"></span>VAST KELP</div>
  <nav class="nav">
    <a class="active" style="left:531px">Home</a>
    <a style="left:589px">About Us</a>
    <a style="left:668px">Our Service</a>
    <a style="left:760px">Who We Are</a>
    <a style="left:849px">Contact Us</a>
  </nav>
  <div class="btn-contact">CONTACT US</div>
</header>

<section class="hero">
  <div class="hero-media" role="img" aria-label="Laboratory microscope with a green leaf, molecular hexagons and a DNA helix on a pale blue background"></div>
  <div class="hero-welcome">Welcome to <span>Vast Kelp</span></div>
  <h1 class="hero-title">Biological <span>Services</span></h1>
  <p class="hero-text">Lorem ipsum dolor sit amet, consectetur adipiscing elit, sed do eiusmod tempor incididunt ut labore et dolore magna aliqua ut enim ad minim.</p>
  <div class="btn-dark">Read More</div>
</section>

<section class="features">
  <div class="feature" style="left:160px">
    <svg width="30" height="30" viewBox="0 0 30 30" fill="none" stroke="#70b02a" stroke-width="1.6"><path d="M9 20H7a5 5 0 0 1 0-10 7 7 0 0 1 13.5-1.5A5.5 5.5 0 0 1 23 20h-2"/><path d="M15 13v12M11 21l4 4 4-4"/></svg>
    <h3>Proin ultrices ex vitae</h3>
    <p>Duis sodales accumsan mollis. In fringilla ex nibh, at egestas ex convallis nec</p>
  </div>
  <div class="feature" style="left:460px">
    <svg width="30" height="30" viewBox="0 0 30 30" fill="none" stroke="#70b02a" stroke-width="1.6"><circle cx="15" cy="15" r="12"/><path d="M9.5 15.5l4 4 7-8"/></svg>
    <h3>Nam velit risus eleifend</h3>
    <p>Mauris dapibus nunc convallis, ullamcorper orci ut, semper risus</p>
  </div>
  <div class="feature" style="left:760px">
    <svg width="30" height="30" viewBox="0 0 30 30" fill="none" stroke="#70b02a" stroke-width="1.6"><rect x="5" y="11" width="20" height="16" rx="1"/><path d="M10 11V8a5 5 0 0 1 10 0v3"/><path d="M11 16h8"/></svg>
    <h3>Sed arcu orci dictum</h3>
    <p>Sed sit amet facilisis tellus. Sed ultrices nibh eget molestie blandit</p>
  </div>
</section>

<section class="about">
  <div class="about-media" role="img" aria-label="Two scientists in lab coats and masks examining a test tube beside a microscope"></div>
  <h2>WHO WE ARE</h2>
  <p style="top:837px">Phasellus justo ligula, dictum sit amet tortor eu, iaculis tristique turpis. Mauris non orci sed est suscipit tempor ut quis felis. Praesent pellentesque at metus eget luctus.</p>
  <p style="top:905px">Mauris congue sem a turpis tempor, eu bibendum magna dapibus. In malesuada. Ligula id condimentum hendrerit, metus tortor tristique quam, ut facilisis tortor purus non nisl. Interdum et malesuada fames ac ante ipsum primis in faucibus. Maecenas venenatis vulputate porta.</p>
  <div class="btn-green">READ MORE</div>
</section>

<section class="grey-band"></section>
<h2 class="section-title" style="left:149px;top:1157px">Latest News</h2>
<div class="pager" style="left:667px;top:1164px">
  <span><svg width="6" height="6" viewBox="0 0 6 6"><path d="M4 0L1 3l3 3" fill="none" stroke="#fff" stroke-width="1.2"/></svg></span>
  <span><svg width="6" height="6" viewBox="0 0 6 6"><path d="M2 0l3 3-3 3" fill="none" stroke="#fff" stroke-width="1.2"/></svg></span>
</div>
<article class="news-card">
  <svg class="abs" style="left:12px;top:18px" width="44" height="48" viewBox="0 0 44 48"><polygon points="22,1 43,13 43,35 22,47 1,35 1,13" fill="#70b02a"/><text x="22" y="22" text-anchor="middle" font-family="Open Sans,sans-serif" font-size="11" fill="#fff">10</text><text x="22" y="35" text-anchor="middle" font-family="Open Sans,sans-serif" font-size="11" fill="#fff">APR</text></svg>
  <p class="news-head">Lorem ipsum dolor sit amet, consectetur adipiscing <em>elit, sed do eiusmod</em> tempor.</p>
  <div class="news-photo" role="img" aria-label="Group of friends smiling outdoors"></div>
  <p class="news-body">Lorem ipsum dolor sit amet, consectetur adipiscing elit, sed do eiusmod tempor incididunt ut labore et dolore magna aliqua. Ut enim ad minim veniam, quis nostrud exercitation ullamco laboris nisi ut aliquip ex ea commodo consequat. Duis aute irure dolor in reprehenderit. In voluptate velit esse</p>
  <p class="news-more">Sed ut perspiciatis unde omnis iste natus error sit voluptatem accusantium doloremque laudantium totam rem aperiam, eaque ipsa quae ab illo inventore veritatis et quasi architecto beatae vitae dicta su</p>
  <div class="scroll-track"></div>
  <div class="scroll-thumb"></div>
</article>

<h2 class="section-title" style="left:720px;top:1157px">Our Testimonials</h2>
<div class="pager" style="left:1022px;top:1164px">
  <span><svg width="6" height="6" viewBox="0 0 6 6"><path d="M4 0L1 3l3 3" fill="none" stroke="#fff" stroke-width="1.2"/></svg></span>
  <span><svg width="6" height="6" viewBox="0 0 6 6"><path d="M2 0l3 3-3 3" fill="none" stroke="#fff" stroke-width="1.2"/></svg></span>
</div>
<blockquote class="quote-card">
  <p><span style="color:#bbb">&ldquo;</span> Lorem ipsum dolor sit amet, consectetuer adipiscing elit, sed do eiusmod tempor incididunt ut labore et dolore magna aliqua. Ut enim ad minim veniam, quis nostrud exercitation ullamco laboris nisi ut aliquip ex ea commodo consequat. Duis aute irure dolor in reprehenderit in voluptate velit esse cillum <span style="color:#bbb">&rdquo;</span></p>
</blockquote>
<svg class="quote-tail" width="24" height="14" viewBox="0 0 24 14"><path d="M0 0h24L4 14z" fill="#fff"/><path d="M0 0L4 14 24 0" fill="none" stroke="#dcdcdc"/></svg>
<div class="avatar" role="img" aria-label="Portrait of the client giving the testimonial"></div>
<div class="person-name">John Doe</div>
<div class="person-place">Perth Austalia</div>

<section class="services">
  <h2>OUR SERVICES</h2>
  <p class="lead">Ut enim ad minim veniam, quis nostrud exercitation ullamco laboris</p>
  <div class="service" style="left:147px">
    <div class="service-art" role="img" aria-label="Illustration of an open book with a plant, flask and DNA strand on a red circle" style="background:linear-gradient(180deg,#e0533f 0%,#e0533f 75%,#6b5a9a 100%)"></div>
    <h3>R &amp; D CENTER</h3>
    <p>Sed ut perspiciatis unde omnis iste natus error sit voluptatem accusantium doloremque laudantium totam rem aperiam, eaque ipsa quae ab illo invent.</p>
    <a>LEARN MORE &rsaquo;</a>
  </div>
  <div class="service" style="left:460px">
    <div class="service-art" role="img" aria-label="Illustration of an open book with a pie chart and test tube on a purple circle" style="background:linear-gradient(180deg,#8f86e0 0%,#7a71d4 75%,#4d4a7a 100%)"></div>
    <h3>R &amp; D CENTER</h3>
    <p>Sed ut perspiciatis unde omnis iste natus error sit voluptatem accusantium doloremque laudantium totam rem aperiam, eaque ipsa quae ab illo invent.</p>
    <a>LEARN MORE &rsaquo;</a>
  </div>
  <div class="service" style="left:774px">
    <div class="service-art" role="img" aria-label="Illustration of an open book with lab glassware and a cactus on a yellow circle" style="background:linear-gradient(180deg,#f1b52e 0%,#f1b52e 75%,#5a5a80 100%)"></div>
    <h3>R &amp; D CENTER</h3>
    <p>Sed ut perspiciatis unde omnis iste natus error sit voluptatem accusantium doloremque laudantium totam rem aperiam, eaque ipsa quae ab illo invent.</p>
    <a>LEARN MORE &rsaquo;</a>
  </div>
</section>

<footer class="site-footer"></footer>
<div class="footer-col">
  <h4 style="left:153px">About Us</h4>
  <p class="footer-about">Lorem ipsum dolor sit amet, consectetur adipiscing elit, sed do eiusmod tempor incididunt ut labore et dolore magna aliqua ut enim ad minim veniam, quis nostrud exercitation ullamco laboris nisi ut aliquip ex ea commodo consequat.</p>

  <h4 style="left:451px">Latrest News</h4>
  <div class="footer-news" style="top:2045px">
    <div class="thumb" role="img" aria-label="Laboratory equipment"></div>
    <div class="t">14 Meadow Row</div>
    <div class="s">Lorem ipsum dolor sit amet, consectetur</div>
    <div class="m">READ MORE</div>
  </div>
  <div class="footer-news" style="top:2116px">
    <div class="thumb" role="img" aria-label="Scientists at work in a lab"></div>
    <div class="t">14 Meadow Row</div>
    <div class="s">Lorem ipsum dolor sit amet, consectetur</div>
    <div class="m">READ MORE</div>
  </div>

  <h4 style="left:769px">Contact us</h4>
  <div class="footer-contact">
    <p style="line-height:18px">82 Harbour Lane, 3rd Floor,<br>Halden, Ontario, K2P4R8</p>
    <p style="margin-top:10px">Phone : (555) 214-0938</p>
    <p style="margin-top:4px">Email : info@vastkelp.com</p>
  </div>

  <h4 style="left:961px">Quick links</h4>
  <ul class="footer-links">
    <li>Home</li><li>About Us</li><li>Service</li><li>Latest News</li><li>Contact Us</li>
  </ul>
</div>

<div class="footer-bottom">
  <span class="copy">Copyright © 2016 VastKelp . com All Right Reserved</span>
  <span class="legal">Terms &amp; Condition &nbsp;&nbsp;|&nbsp;&nbsp; Privacy Policy</span>
</div>

</body>
</html>
```